Fatigued and Overloaded by COVID Messages? We need original illustrations to show that.

Everywhere you look there are messages about COVID. That is leading many people to feel fatigued and overloaded by the messages.

We surveyed U.S. adults March 20th - 24th, 2020 and measured message fatigue, information overload, perceived repetition, and perceived exaggeration. Here is how participants responded:

When it comes to coronavirus . . .
55% feel exhausted by all the messages.
54% feel overloaded by the amount of information.
51% feel that the messages are repetitive.
47% feel like messages exaggerate how bad it is.

In other words, almost half of U.S. adults show signs of message fatigue, information overload, perceived message repetition, and perceived message exaggeration.

We will continue to survey 400 adults every week for the next 16 weeks. Each time we will measure message fatigue, information overload, perceived repetition, and perceived exaggeration. We expect that it will increase over time.

What are we looking for? We need innovative and original illustrations that attempt to communicate these findings. The illustrations would visualize message fatigue, information overload, perceived message repetition, and perceived message exaggeration.

What sort of visual are we looking for? Our preference is for an original illustration (or set of illustrations). Our preference is for creative and powerful illustrations, but we are also open to the creative and well-executed infographics.

We need these images fast . We will award monetary prizes to the 3 best designs. If we like more than that, then we might purchase more (e.g., in past contests, we have purchased as many as 30 designs).

What we will need:
(1) The illustrations must be original and we will need the photoshop and/or illustrator files for all artwork. (By original, we mean that the illustrations are 100% created by you. Our organization requires that we utilize only original illustrated work. We have had issues with free imagery being pirated and reposted as free. We sidestep that issue by just having everything created.)

(2) The illustration should say, somewhere: "Based on a survey of 400 U.S. adults conducted March 20 - 24th, 2020."

(3) We will have almost 4 months worth of data by the time this is done. In other words, the illustrations might be able to help us present that weekly data.

(4) We have conducted other Artvendo projects. It might be helpful to examine designs we liked in the past. For example, here is another COVID project we just finished:

https://jobs.artvendo-example.com/job/5162048

Target Market(s)

U.S. adults

Requirements
Must have
• Original illustrations. Mobile friendly design. People will view this on their smartphones.
Nice to have
• A design that we can use to communicate the data across time.

```html
<!DOCTYPE html>
<html lang="en">
<head>
<meta charset="utf-8">
<title>When it comes to Coronavirus – Message Fatigue Survey</title>
<link rel="stylesheet" href="https://fonts.googleapis.com/css2?family=Heebo:wght@400;500;600;700&display=swap">
<style>
  :root {
    --red-top: #66191c;
    --red-mid: #c62f31;
    --red-low: #a93033;
    --navy-top: #1f1f2b;
    --navy-mid: #34334a;
    --navy-low: #4a4868;
    --band: rgba(58, 52, 78, 0.72);
    --ink: #f7f7fa;
    --muted: #c9c7cf;
  }
  * { margin: 0; padding: 0; box-sizing: border-box; }
  html, body { width: 1200px; height: 998px; overflow: hidden; }
  body { font-family: "Heebo", "Helvetica Neue", Arial, sans-serif; color: var(--ink); }

  .poster { position: relative; width: 1200px; height: 998px; overflow: hidden; }

  .columns { position: absolute; inset: 0; display: flex; }
  .column { width: 300px; height: 100%; }
  .column--red { background: linear-gradient(180deg, var(--red-top) 0%, var(--red-mid) 48%, var(--red-low) 100%); }
  .column--navy { background: linear-gradient(180deg, var(--navy-top) 0%, var(--navy-mid) 45%, var(--navy-low) 75%, var(--navy-mid) 100%); }

  .art-band {
    position: absolute; left: 230px; top: 428px; width: 970px; height: 258px;
    background: linear-gradient(90deg, rgba(58,52,78,0) 0%, var(--band) 14%, var(--band) 100%);
    border-radius: 40px 0 0 60px;
  }

  .title {
    position: absolute; top: 30px; left: 0; width: 1222px; text-align: center;
    font-size: 47px; font-weight: 500; letter-spacing: 0.3px;
  }

  .stat {
    position: absolute; top: 140px; width: 300px; text-align: center; line-height: 1;
  }
  .stat:nth-of-type(1) { left: 14px; }
  .stat__value { font-size: 100px; font-weight: 700; letter-spacing: -2px; line-height: 0.95; }
  .stat__label { margin-top: 2px; }
  .stat__label span { display: block; }
  .small { font-size: 18px; font-weight: 500; }
  .big { font-size: 33px; font-weight: 500; letter-spacing: 0.5px; }
  .mid { font-size: 26px; font-weight: 600; }
  .sup { font-size: 18px; font-weight: 500; vertical-align: 12px; margin-right: 3px; }

  .stat--exhausted { left: 14px; }
  .stat--overloaded { left: 305px; top: 146px; }
  .stat--repetitive { left: 603px; top: 152px; }
  .stat--exaggerate { left: 897px; top: 152px; }

  .summary {
    position: absolute; right: 120px; top: 463px; text-align: right;
    font-size: 37px; font-weight: 600; line-height: 48px; letter-spacing: 0.2px;
  }
  .source {
    position: absolute; right: 135px; top: 700px; text-align: right;
    font-size: 22px; font-weight: 500; line-height: 29px; color: var(--muted);
  }
</style>
</head>
<body>
<main class="poster">
  <div class="columns" aria-hidden="true">
    <div class="column column--red"></div>
    <div class="column column--navy"></div>
    <div class="column column--red"></div>
    <div class="column column--navy"></div>
  </div>

  <div class="art-band" role="img" aria-label="Brush-stroke illustration of megaphones and message bubbles spreading across the columns"></div>

  <h1 class="title">When it comes to Coronavirus...</h1>

  <section class="stat stat--exhausted">
    <div class="stat__value">55%</div>
    <div class="stat__label">
      <span><span class="sup">feel</span><span class="big">EXAUSTED</span></span>
      <span class="small">by all the</span>
      <span class="mid">messages</span>
    </div>
  </section>

  <section class="stat stat--overloaded">
    <div class="stat__value">54%</div>
    <div class="stat__label">
      <span><span class="sup">feel</span><span class="big">OVERLOADED</span></span>
      <span class="small">by the amount</span>
      <span class="mid">of information</span>
    </div>
  </section>

  <section class="stat stat--repetitive">
    <div class="stat__value">51%</div>
    <div class="stat__label">
      <span><span class="small">feel the </span><span class="mid">messages</span></span>
      <span><span class="sup">are</span><span class="big">REPETITIVE</span></span>
    </div>
  </section>

  <section class="stat stat--exaggerate">
    <div class="stat__value">47%</div>
    <div class="stat__label">
      <span><span class="small">feel like </span><span class="mid">messages</span></span>
      <span class="big">EXAGGERATE</span>
      <span class="mid">how bad it is</span>
    </div>
  </section>

  <p class="summary">
    In other words, almost half of U.S adults<br>
    show signs of message fatigue,<br>
    information overload, perceived message repetition,<br>
    and perceived message exaggeration.
  </p>

  <p class="source">
    Based on a survey of 400 U.S adults<br>
    coducted March 20 - 24th, 2020
  </p>
</main>
</body>
</html>
```